Business Card Design Project

We need a business card to reflect the design of our website - just so it all ties in - it has a retro feel and can be found at http://www.lunetaswingduo.com
We will need our phone 0493 215 764
Web address, and email lunetaduo@corvanet.com included
Our catch cry is "Classic Cocktail Music"
Perfect Live Music for Private & Corporate Events, Weddings and Dinner Music
Our names should be included :-
Deborah Feltham / piano & Owen Lockett / bass
I am now also including our logo so that it can be included (in part or whole) somehow in the design
My partner thinks we should include our logo in some form in the design of the card - i will attach this here for you. I will attach eps but if you prefer another format please let me know
Regards
Debbie

```html
<!DOCTYPE html>
<html lang="en">
<head>
<meta charset="utf-8">
<title>Luneta Duo – Business Card</title>
<link href="https://fonts.googleapis.com/css2?family=Josefin+Sans:wght@300;400;600&family=Sniglet:wght@800&display=swap" rel="stylesheet">
<style>
  :root {
    --backdrop: #d9d6cf;
    --teal: #8cc6c9;
    --teal-deep: #6aa8ac;
    --cream: #e7e3d7;
    --ribbon: #f4eedc;
    --ribbon-fold: #d8ceb3;
    --ink: #2e2e2e;
    --ink-soft: #444;
    --white: #ffffff;
    --badge: #4b4b4b;
  }
  * { box-sizing: border-box; margin: 0; padding: 0; }
  html, body { width: 1200px; height: 800px; overflow: hidden; }
  body {
    background: var(--backdrop);
    font-family: "Josefin Sans", sans-serif;
    color: var(--ink);
  }
  .card {
    position: absolute;
    left: 100px; top: 100px;
    width: 1000px; height: 600px;
    background: var(--cream);
    box-shadow: 0 10px 30px rgba(0,0,0,.18);
    overflow: hidden;
  }
  .card__header { position: absolute; left: 0; top: 0; width: 1000px; height: 210px; }
  .nav {
    position: absolute; top: 38px;
    display: flex; gap: 48px;
    font-family: "Sniglet", sans-serif; font-weight: 800;
    font-size: 26px; letter-spacing: 1px;
    color: var(--white); text-transform: uppercase;
  }
  .nav--left { left: 50px; }
  .nav--right { right: 50px; }
  .name {
    position: absolute; top: 206px; width: 100%;
    text-align: center;
    font-weight: 300; font-size: 52px; letter-spacing: 5px;
    color: var(--teal-deep); text-transform: uppercase;
  }
  .dots {
    position: absolute; top: 296px; height: 8px;
    background-image: radial-gradient(circle, #fbf9f3 2.5px, transparent 3px);
    background-size: 24px 8px;
  }
  .dots--left { left: 120px; width: 170px; }
  .dots--right { right: 120px; width: 170px; }
  .tagline { position: absolute; left: 250px; top: 262px; width: 500px; height: 86px; }
  .tagline__text {
    position: absolute; left: 0; top: 27px; width: 500px;
    text-align: center;
    font-family: "Sniglet", sans-serif; font-weight: 800;
    font-size: 30px; letter-spacing: 1px;
    color: var(--ink); text-transform: uppercase;
  }
  .website {
    position: absolute; top: 356px; width: 100%;
    text-align: center;
    font-size: 24px; letter-spacing: 2px; color: var(--ink-soft);
    text-transform: uppercase;
  }
  .card__footer { position: absolute; left: 0; top: 450px; width: 1000px; height: 150px; background: var(--teal); }
  .card__footer::before {
    content: ""; position: absolute; left: 0; right: 0; top: 12px;
    border-top: 2px dashed var(--teal-deep);
  }
  .label { font-family: "Sniglet", sans-serif; font-weight: 800; text-transform: uppercase; letter-spacing: 1px; }
  .team { position: absolute; left: 40px; top: 44px; font-size: 21px; }
  .contact { position: absolute; left: 620px; top: 66px; font-size: 21px; line-height: 30px; }
</style>
</head>
<body>
  <div class="card">
    <svg class="card__header" viewBox="0 0 1000 210" aria-hidden="true">
      <path d="M0 0 H1000 V120 H587.4 A88 88 0 0 1 412.6 120 H0 Z" fill="var(--teal)"/>
      <path d="M0 108 H422 A78 78 0 1 0 578 108 H1000" fill="none" stroke="var(--teal-deep)" stroke-width="2" stroke-dasharray="6 5"/>
      <circle cx="500" cy="110" r="72" fill="var(--teal-deep)"/>
      <circle cx="500" cy="110" r="66" fill="var(--badge)"/>
    </svg>

    <nav class="nav nav--left"><span>About us</span><span>Portfolio</span></nav>
    <nav class="nav nav--right"><span>Blog</span><span>Hire us</span></nav>

    <h1 class="name">Luneta Duo</h1>

    <div class="dots dots--left"></div>
    <div class="dots dots--right"></div>

    <div class="tagline">
      <svg width="500" height="86" viewBox="0 0 500 86" aria-hidden="true">
        <path d="M0 30 H60 V80 H0 L18 55 Z" fill="var(--ribbon-fold)"/>
        <path d="M500 30 H440 V80 H500 L482 55 Z" fill="var(--ribbon-fold)"/>
        <path d="M40 66 L60 80 V66 Z" fill="#b9ae92"/>
        <path d="M460 66 L440 80 V66 Z" fill="#b9ae92"/>
        <rect x="40" y="14" width="420" height="52" fill="var(--ribbon)"/>
      </svg>
      <p class="tagline__text">Classic Cocktail Music</p>
    </div>

    <p class="website">www.lunetaswingduo.com</p>

    <footer class="card__footer">
      <p class="team"><span class="label">Team</span> : Deborah Feltham / piano &amp; Owen Lockett / bass</p>
      <p class="contact">
        <span class="label">Phone</span> : 0493 215 764<br>
        <span class="label">Email</span> : lunetaduo@corvanet.com
      </p>
    </footer>
  </div>
</body>
</html>
```